50th Anniversary Gala Save the date Postcard 8.5x5.5 inches

Looking for a 5.5x8.5 in one-sided postcard design for our annual gala. Design needs to include "Save the date" prominently with all the event information included below. Design should be light, include the colors of our logo and elegant. (almost like a wedding save the date). "Bridges of Grace" should look like its own logo.

50th Anniversary Gala at The Lodge at Birchmere Glen – “Bridges of Grace – Celebrating 50 Years of Building Community”
Thursday, October 24
6-11p
The Lodge at Birchmere Glen
Calloway Parkway, Maple Hollow, CT
Honoring – TRB Previous Presidents

Target Market(s)

Exisiting donors

Industry/Entity Type

nonprofit

Font styles to use
Serif
Script

Requirements
Must have
• Save the date prominent
Should not have
• should not have a dark background

```html
<!DOCTYPE html>
<html lang="en">
<head>
<meta charset="utf-8">
<title>Save The Date – 50th Anniversary Gala</title>
<link rel="stylesheet" href="https://fonts.googleapis.com/css2?family=Pinyon+Script&family=Roboto+Slab:wght@300;400;700;800&display=swap">
<style>
  :root {
    --frame-blue: #2b8fd1;
    --card-white: #ffffff;
    --ink: #1f1f1f;
    --script-grey: #8a8a8a;
    --navy: #1d4f91;
    --sky: #2a8bd0;
    --gold: #c9a444;
    --gold-line: #d2b15a;
    --logo-green: #5aae3c;
  }
  * { box-sizing: border-box; margin: 0; padding: 0; }
  html, body { width: 1200px; height: 820px; overflow: hidden; background: #f3f3f1; }
  .postcard {
    width: 1200px; height: 820px;
    background: var(--frame-blue);
    padding: 16px;
  }
  .postcard-face {
    width: 100%; height: 100%;
    background: radial-gradient(ellipse at center, #ffffff 55%, #f4f5f6 100%);
    display: flex; flex-direction: column; align-items: center; justify-content: center;
    font-family: "Roboto Slab", Georgia, serif;
    color: var(--ink);
    text-align: center;
  }
  .brand { display: flex; align-items: center; gap: 14px; }
  .brand-dot { width: 22px; height: 22px; border-radius: 50%; background: var(--logo-green); }
  .brand-name { font-size: 42px; line-height: 50px; font-weight: 700; color: var(--navy); letter-spacing: 0.5px; }
  .anniversary-years {
    display: flex; align-items: center; gap: 14px;
    margin-top: 12px; font-size: 20px; line-height: 24px; font-weight: 400; color: var(--navy); letter-spacing: 4px;
  }
  .anniversary-years .rule { width: 120px; height: 2px; background: var(--gold-line); }
  .save-the-date {
    font-family: "Pinyon Script", cursive;
    font-size: 104px; font-weight: 400; color: var(--script-grey); line-height: 1.15; margin-top: 12px;
  }
  .gala-line { font-size: 30px; line-height: 40px; font-weight: 400; margin-top: 8px; }
  .gala-theme { font-size: 36px; line-height: 46px; font-weight: 800; color: var(--navy); letter-spacing: 1px; margin-top: 6px; }
  .gala-tagline { font-size: 30px; line-height: 40px; font-weight: 400; margin-top: 6px; }
  .date-ribbon { position: relative; width: 720px; height: 74px; margin-top: 24px; }
  .date-ribbon svg { position: absolute; inset: 0; }
  .date-ribbon span {
    position: relative; display: block; line-height: 74px;
    font-size: 34px; font-weight: 800; color: #fff; letter-spacing: 1px;
  }
  .venue-name { font-size: 30px; line-height: 40px; font-weight: 700; color: var(--sky); margin-top: 18px; }
  .venue-address { font-size: 30px; line-height: 40px; font-weight: 300; color: var(--navy); margin-top: 4px; }
  .honoring { font-size: 24px; line-height: 32px; font-weight: 400; margin-top: 10px; }
</style>
</head>
<body>
  <main class="postcard">
    <section class="postcard-face">
      <div class="brand">
        <span class="brand-dot"></span>
        <span class="brand-name">Harbor Connections</span>
      </div>
      <div class="anniversary-years">
        <span class="rule"></span><span>1974 – 2024</span><span class="rule"></span>
      </div>

      <h1 class="save-the-date">Save The Date</h1>

      <p class="gala-line">50th Anniversary Gala at The Lodge at Birchmere Glen</p>
      <p class="gala-theme">BRIDGES OF GRACE</p>
      <p class="gala-tagline">Celebrating 50 Years of Building Community</p>

      <div class="date-ribbon">
        <svg viewBox="0 0 720 74" width="720" height="74" aria-hidden="true">
          <polygon points="0,0 720,0 696,37 720,74 0,74 24,37" fill="var(--gold)"/>
        </svg>
        <span>THURSDAY, OCTOBER 24, 6-11P</span>
      </div>

      <p class="venue-name">The Lodge at Birchmere Glen</p>
      <p class="venue-address">Calloway Parkway, Maple Hollow, CT</p>
      <p class="honoring">Honoring – TRB Previous Presidents</p>
    </section>
  </main>
</body>
</html>
```